Disposable Mini Sauce Pot Design for Asian Chain Food Brands

We operate a Hainan Chicken Rice takeout brand under the name Spin4Rye, with our official website: www.Spin4Rye.com.
We offer four signature house sauces and are launching brand-new packaging for our sauce line. We require custom graphic designs exclusively for the sauce cup lids.
Product Material & Base Specs
The sauce cups are made of PP plastic, available in two translucent base options: Translucent White and Translucent Orange.
Four Sauce Varieties for Individual Lid Designs
1. Red Sauce – Fried Sweet Chili Sauce
2.Green Sauce – Scallion Oil Dressing
3.Sweet Soy Sauce
4.Sweet Red Sauce (Special for Fried Chicken)
Differentiate each sauce lid design through unique graphics, typography, or illustrative elements for easy customer identification.
The marking NET WT 2 OZ must be clearly printed on every lid.
**There is no need to print full descriptive text or the full name of the sauces on each lid; the design only needs to clearly differentiate the four sauce varieties.
**Please reference the original design style and brand color palette shown on our official website, and feel free to fully unleash your creativity.

```html
<!DOCTYPE html>
<html lang="en">
<head>
<meta charset="utf-8">
<title>Spin4Rye Sauce Lid Labels</title>
<link href="https://fonts.googleapis.com/css2?family=Sriracha&family=Montserrat:wght@400;800&display=swap" rel="stylesheet">
<style>
  :root {
    --page: #ffffff;
    --ink: #ffffff;
    --red: #ff2a00;
    --red-shade: #c81a06;
    --green: #a6d900;
    --green-shade: #80a800;
    --orange: #e97d33;
    --orange-shade: #c9521a;
    --pink: #ec0a84;
    --pink-shade: #c21d52;
  }
  * { margin: 0; padding: 0; box-sizing: border-box; }
  html, body { width: 720px; height: 1200px; overflow: hidden; background: var(--page); }
  .lid-sheet {
    position: relative;
    width: 720px; height: 1200px;
    display: grid;
    grid-template-columns: 320px 320px;
    grid-template-rows: 362px 362px;
    gap: 30px;
    justify-content: center;
    align-content: center;
  }
  .lid {
    position: relative;
    border-radius: 40px;
    overflow: hidden;
    color: var(--ink);
    text-align: center;
    font-family: "Sriracha", cursive;
  }
  .lid--red { background: var(--red); --shade: var(--red-shade); }
  .lid--green { background: var(--green); --shade: var(--green-shade); }
  .lid--orange { background: var(--orange); --shade: var(--orange-shade); }
  .lid--pink { background: var(--pink); --shade: var(--pink-shade); }
  .lid__art {
    position: absolute; left: 0; top: 108px;
    width: 320px; height: 254px;
  }
  .brand { position: absolute; left: 30px; top: 18px; text-align: left; }
  .brand__name { font-size: 46px; line-height: 1; }
  .brand__tag {
    font-family: "Montserrat", sans-serif; font-weight: 800;
    font-size: 13px; letter-spacing: 0.5px; margin-top: 4px;
  }
  .sauce { position: absolute; left: 0; right: 0; }
  .sauce__name { font-size: 50px; line-height: 1; }
  .sauce__note { font-size: 24px; line-height: 1; margin-top: 14px; }
  .net-wt {
    position: absolute; left: 0; right: 0; top: 298px;
    font-family: "Montserrat", sans-serif; font-weight: 400; font-size: 15px; letter-spacing: 0.5px;
  }
  .site { position: absolute; left: 0; right: 0; top: 318px; font-size: 16px; }
</style>
</head>
<body>
<main class="lid-sheet">

  <section class="lid lid--red">
    <svg class="lid__art" role="img" aria-label="Chicken silhouette with chili pepper illustration" viewBox="0 0 320 254"><path d="M0 110 Q40 60 90 40 Q120 0 170 20 Q200 40 190 90 Q270 60 300 20 L320 60 L320 200 Q200 250 0 254 Z" fill="var(--shade)" opacity="0.55"/></svg>
    <div class="brand"><div class="brand__name">Spin4Rye</div><div class="brand__tag">HAINAN CHICKEN</div></div>
    <div class="sauce" style="top:172px"><div class="sauce__name">Red Sauce</div><div class="sauce__note">Fried Sweet Chili Sauce</div></div>
    <div class="net-wt">NET WT 2 OZ</div>
    <div class="site">www.Spin4Rye.com</div>
  </section>

  <section class="lid lid--green">
    <svg class="lid__art" role="img" aria-label="Chicken silhouette with scallion illustration" viewBox="0 0 320 254"><path d="M0 110 Q40 60 90 40 Q120 0 170 20 Q200 40 190 90 Q270 60 300 20 L320 60 L320 200 Q200 250 0 254 Z" fill="var(--shade)" opacity="0.55"/></svg>
    <div class="brand"><div class="brand__name">Spin4Rye</div><div class="brand__tag">HAINAN CHICKEN</div></div>
    <div class="sauce" style="top:172px"><div class="sauce__name">Green Sauce</div><div class="sauce__note">Scallion Oil Dressing</div></div>
    <div class="net-wt">NET WT 2 OZ</div>
    <div class="site">www.Spin4Rye.com</div>
  </section>

  <section class="lid lid--orange">
    <svg class="lid__art" role="img" aria-label="Chicken silhouette with soybean pod illustration" viewBox="0 0 320 254"><path d="M0 110 Q40 60 90 40 Q120 0 170 20 Q200 40 190 90 Q270 60 300 20 L320 60 L320 200 Q200 250 0 254 Z" fill="var(--shade)" opacity="0.55"/></svg>
    <div class="brand"><div class="brand__name">Spin4Rye</div><div class="brand__tag">HAINAN CHICKEN</div></div>
    <div class="sauce" style="top:168px"><div class="sauce__name">Sweet Soy<br>Sauce</div></div>
    <div class="net-wt">NET WT 2 OZ</div>
    <div class="site">www.Spin4Rye.com</div>
  </section>

  <section class="lid lid--pink">
    <svg class="lid__art" role="img" aria-label="Chicken silhouette with tomato illustration" viewBox="0 0 320 254"><path d="M0 110 Q40 60 90 40 Q120 0 170 20 Q200 40 190 90 Q270 60 300 20 L320 60 L320 200 Q200 250 0 254 Z" fill="var(--shade)" opacity="0.55"/></svg>
    <div class="brand"><div class="brand__name">Spin4Rye</div><div class="brand__tag">HAINAN CHICKEN</div></div>
    <div class="sauce" style="top:160px"><div class="sauce__name">Sweet Red<br>Sauce</div><div class="sauce__note" style="font-size:22px;margin-top:6px">Special for Fried Chicken</div></div>
    <div class="net-wt">NET WT 2 OZ</div>
    <div class="site">www.Spin4Rye.com</div>
  </section>

</main>
</body>
</html>
```